Coastal Bright Sweep Business Card

We are a cleaning and waste management company with the slogan "making waste to landfill a thing of the past". We would like a re-design of our current business card. On the front we want to continue to use our logo as the focus point. On the back, we want the whole thing re-done to be less busy. We want the staff member’s name, the job title, mobile number, email and website. We do not want the address on the card. We still want the green, black and blue colours used, but a new font for the information on the back. Please do not change the logo design at all. We are also thinking about using icons to replace the text ‘mobile, email, website’. The “events + commercial” banner needs to be incorporated somewhere and needs to read “events + commercial + waste”. Another important point for consideration is that we are very concerned about being environmentally sustainable and will be printing on recycled paper. All designs should be made to compliment this in regards to boldness and colouring. Please find attached our logo, our colour chart and an image of our current business card.

```html
<!DOCTYPE html>
<html lang="en">
<head>
<meta charset="utf-8">
<title>Coastal Bright Sweep Business Card</title>
<link href="https://fonts.googleapis.com/css2?family=Cinzel:wght@500&family=Open+Sans:wght@400;700&display=swap" rel="stylesheet">
<style>
  :root {
    --bg: #e6e6e6;
    --card: #ffffff;
    --green: #7cc242;
    --green-dark: #5fa02e;
    --navy: #1b3f73;
    --ink: #222222;
    --white: #ffffff;
    --shadow: rgba(0,0,0,0.22);
  }
  * { box-sizing: border-box; margin: 0; padding: 0; }
  html, body { width: 1200px; height: 874px; overflow: hidden; }
  body {
    background: var(--bg);
    font-family: "Open Sans", Arial, sans-serif;
    position: relative;
  }
  .card {
    position: absolute;
    left: 320px;
    width: 560px;
    height: 342px;
    background: var(--card);
    box-shadow: 0 4px 14px var(--shadow);
    overflow: hidden;
  }
  .card--back { top: 65px; }
  .card--front { top: 467px; }

  .wordmark {
    position: absolute;
    font-family: "Open Sans", Arial, sans-serif;
    font-weight: 700;
    color: var(--navy);
    line-height: 1.05;
    text-align: center;
  }
  .card--back .wordmark { left: 30px; top: 96px; width: 200px; font-size: 30px; }
  .card--front .wordmark { left: 130px; top: 100px; width: 300px; font-size: 44px; }

  .info-panel {
    position: absolute;
    left: 245px; top: 36px;
    width: 320px; height: 241px;
    box-shadow: -6px 0 8px -4px var(--shadow);
    background: var(--card);
  }
  .name-band {
    position: absolute;
    left: 243px; top: 84px;
    width: 317px; height: 62px;
    background: var(--green);
    color: var(--white);
    padding: 8px 0 0 46px;
  }
  .name-band__name {
    font-family: "Cinzel", Georgia, serif;
    font-weight: 500;
    font-size: 24px;
    line-height: 1.1;
  }
  .name-band__title { font-size: 16px; line-height: 1.3; }

  .contact {
    position: absolute;
    left: 268px; top: 180px;
    color: var(--ink);
    list-style: none;
  }
  .contact__row { display: flex; align-items: flex-start; }
  .contact__row + .contact__row { margin-top: 6px; }
  .contact__icon { width: 14px; height: 14px; margin: 2px 10px 0 0; flex: none; }
  .contact__text { font-size: 13px; line-height: 17px; white-space: nowrap; }
  .contact__text--small { font-size: 11.5px; line-height: 17px; }

  .fold { position: absolute; left: 516px; top: 258px; width: 44px; height: 20px; }

  .tagline-band {
    position: absolute;
    left: 0; top: 277px;
    width: 560px; height: 35px;
    background: var(--green);
    color: var(--white);
    font-size: 18px;
    line-height: 35px;
    text-align: center;
    letter-spacing: 0.2px;
  }
</style>
</head>
<body>

<section class="card card--back" aria-label="Business card, contact side">
  <div class="wordmark">Coastal<br>Bright<br>Sweep</div>
  <div class="info-panel"></div>
  <div class="name-band">
    <p class="name-band__name">Marla Quenby</p>
    <p class="name-band__title">Client Manager</p>
  </div>
  <ul class="contact">
    <li class="contact__row">
      <svg class="contact__icon" viewBox="0 0 14 14" aria-hidden="true"><circle cx="7" cy="7" r="6" fill="none" stroke="#222" stroke-width="1.2"/><path d="M4.5 9.5 L9.5 4.5" stroke="#222" stroke-width="2"/></svg>
      <span class="contact__text">0400 555 218</span>
    </li>
    <li class="contact__row">
      <svg class="contact__icon" viewBox="0 0 14 14" aria-hidden="true"><rect x="1" y="3" width="12" height="8" fill="none" stroke="#222" stroke-width="1.1"/><path d="M1 3 L7 8 L13 3" fill="none" stroke="#222" stroke-width="1.1"/></svg>
      <span class="contact__text contact__text--small">mquenby@coastalbrightsweep.com.au</span>
    </li>
    <li class="contact__row">
      <svg class="contact__icon" viewBox="0 0 14 14" aria-hidden="true"><circle cx="7" cy="7" r="5.5" fill="none" stroke="#222" stroke-width="1.1"/><path d="M1.5 7 H12.5 M7 1.5 C4 5 4 9 7 12.5 C10 9 10 5 7 1.5" fill="none" stroke="#222" stroke-width="1"/></svg>
      <span class="contact__text contact__text--small">www.coastalbrightsweep.com.au</span>
    </li>
  </ul>
  <svg class="fold" viewBox="0 0 44 20" aria-hidden="true"><polygon points="0,8 18,0 44,20 0,20" fill="#5fa02e"/><polygon points="18,0 44,20 30,20" fill="#7cc242"/></svg>
  <div class="tagline-band">EVENTS + COMMERCIAL + WASTE</div>
</section>

<section class="card card--front" aria-label="Business card, name side">
  <div class="wordmark">Coastal<br>Bright<br>Sweep</div>
</section>

</body>
</html>
```